Frame Design for a collection of Tarot Cards

Update 1: I've added a drawing showing a corner of the framed collection. Note that the name of the character depicted on the tarot card is included below the card and not on the card itself. There will also be some space to include a few of lines of text about the person shown on the card.
Update 2: While it will be nice to see some examples of tarot cards contained within the frame, we are not expecting you to design cards at this stage.
-----------------------------
We need some graphic designs for framed collections of tarot cards.
The frames will be quite retro - probably looking like wood that has a distressed paint finish.
All the cards, except one, will be normal sized tarot cards that, in the finished product, will be back lit. One card will be extra large (see rough sketch) and will also be back lit.
Above the large central tarot card will be a screen that in default mode will show the back of a tarot card.
Beneath the large tarot card will be a circular recess that will display one of the platonic solids. In this design it will contain a dodecahedron.
Please note that we will be producing other picture frames containing 4, 6, 8, and 20 of the smaller tarot cards.
The cards will all be under glass that is held in place by the frame.
The keyhole will also be under the glass.
Ultimately, we will be producing 30 of these framed tarot card collections.
The tarot cards will be bespoke, that is to say they will look like old fashioned tarot cards, but they will depict people associated with the city of Cambridge (such as Walter Fenwick, Gordon Millbray, Lou Kimble et al).
The graphic design will be used within a presentation pack to illustrate the look and feel of a new bar that is under construction in Cambridge, UK. The idea is to create a basement gallery that is also a cocktail bar.
We welcome ideas for how the mount board for the cards should look.
At this stage we recommend showing us some sample ideas of how you think the framed collection might look. If we think you are on the right track, we will let you know. We don't want you putting in a lot of work that might not come to anything.
Once we have a design that we think is on the right track, we will increase the budget for the project by at least £100.

```html
<!DOCTYPE html>
<html lang="en">
<head>
<meta charset="utf-8">
<title>Framed Tarot Collection – Walter Fenwick</title>
<link rel="stylesheet" href="https://fonts.googleapis.com/css2?family=Cormorant+SC:wght@600&family=Open+Sans:wght@400&display=swap">
<style>
  :root {
    --page: #ffffff;
    --backdrop: #241a12;
    --ribbed: #1c1511;
    --ribbed-hi: #2e241d;
    --shell-deep: #2a0806;
    --shell-red: #7a1a12;
    --shell-warm: #9c2a18;
    --gold: #b58a3c;
    --gold-dark: #6f4f1c;
    --mount-top: #bfae9e;
    --mount-bottom: #ebe3d9;
    --panel: #ffffff;
    --panel-edge: #b9aea4;
    --recess: #f4efe8;
    --recess-edge: #cbbfb2;
    --ink: #2b2622;
    --card-tone: #c9a6a8;
    --card-tone-2: #e9dccb;
  }
  * { margin: 0; padding: 0; box-sizing: border-box; }
  html, body { width: 1052px; height: 1200px; overflow: hidden; background: var(--page); }
  .canvas { position: relative; width: 1052px; height: 1200px; }

  .backdrop { position: absolute; left: 112px; top: 113px; width: 824px; height: 969px; background: var(--backdrop); }

  .frame { position: absolute; left: 129px; top: 130px; width: 795px; height: 935px; }
  .frame-layer { position: absolute; }
  .edge-outer { inset: 0; background: var(--ribbed); }
  .shell-outer { inset: 11px; background: linear-gradient(135deg, var(--shell-red), var(--shell-deep) 30%, var(--shell-warm) 55%, var(--shell-deep) 80%, var(--shell-red)); }
  .edge-mid { inset: 60px; background: linear-gradient(180deg, var(--ribbed-hi), var(--ribbed)); }
  .shell-inner { inset: 78px; background: linear-gradient(160deg, var(--shell-deep), var(--shell-red) 40%, var(--shell-deep) 70%, var(--shell-warm)); }
  .moulding { inset: 120px; background: linear-gradient(135deg, var(--ribbed-hi), var(--ribbed) 50%, #120d0a); }
  .gold-lip { inset: 172px; background: linear-gradient(135deg, var(--gold), var(--gold-dark) 50%, var(--gold)); }
  .mount { inset: 181px; background: linear-gradient(180deg, var(--mount-top), var(--mount-bottom)); }

  .panel { position: absolute; left: 364px; top: 374px; width: 320px; height: 386px; background: var(--panel); border: 1px solid var(--panel-edge); box-shadow: 0 0 3px rgba(0,0,0,0.25); }

  .card-display { position: absolute; left: 366px; top: 393px; width: 172px; height: 364px; background: linear-gradient(170deg, #1a1a1a 0%, #2b2b2b 45%, var(--card-tone) 60%, var(--card-tone-2) 100%); }

  .solid-recess { position: absolute; left: 574px; top: 441px; width: 54px; height: 54px; border-radius: 50%; background: var(--recess); border: 1px solid var(--recess-edge); }

  .caption { position: absolute; font-family: "Cormorant SC", serif; font-weight: 600; color: var(--ink); font-size: 7.5px; text-align: center; letter-spacing: 0.2px; line-height: 9.5px; }
  .speaker-label { left: 540px; top: 500px; width: 122px; }
  .card-small { position: absolute; left: 558px; top: 538px; width: 85px; height: 123px; background: linear-gradient(180deg, var(--card-tone-2), var(--card-tone) 70%, var(--card-tone-2)); border: 1px solid #a88d7c; }
  .name-label { left: 540px; top: 663px; width: 122px; }

  .bio { position: absolute; left: 386px; top: 776px; width: 280px; font-family: "Open Sans", sans-serif; font-size: 5.4px; line-height: 6.4px; color: var(--ink); text-indent: 5px; }
</style>
</head>
<body>
<div class="canvas">
  <div class="backdrop"></div>
  <div class="frame">
    <div class="frame-layer edge-outer"></div>
    <div class="frame-layer shell-outer"></div>
    <div class="frame-layer edge-mid"></div>
    <div class="frame-layer shell-inner"></div>
    <div class="frame-layer moulding"></div>
    <div class="frame-layer gold-lip"></div>
    <div class="frame-layer mount"></div>
  </div>

  <div class="panel"></div>
  <div class="card-display" role="img" aria-label="Screen above a large tarot card showing a portrait of Walter Fenwick"></div>

  <div class="solid-recess" role="img" aria-label="Circular recess for a platonic solid"></div>
  <p class="caption speaker-label">Speaker: Lorem ipsum</p>

  <div class="card-small" role="img" aria-label="Tarot card showing a portrait of Walter Fenwick"></div>
  <p class="caption name-label">Name:&nbsp; Walter Fenwick<br>1643 - 1726</p>

  <p class="bio">Lorem ipsum dolor sit amet, consectetuer adipiscing elit, sed diam nonummy nibh euismod tincidunt ut laoreet dolore magna aliquam erat volutpat. Ut wisi enim ad minim veniam, quis nostrud exerci tation ullamcorper suscipit lobortis nisl ut aliquip ex ea commodo consequat.</p>
</div>
</body>
</html>
```